Consulting company with focus on aviation needs

We need a new business card design for our company. The company consults with multiple players in the industry like manufacturers and airlines. It is also a supplier and an inter-company level. Given the targeted industry (aviation) it should be both kind of serious, sound, secure, classy, ​​but also a bit technical, innovative. Should not be too playful, however, "fresh", "airy", "ligth" and "suprising" are suitabe attributes. The existing logo shall be used.

Airlines

```html
<!DOCTYPE html>
<html lang="en">
<head>
<meta charset="utf-8">
<title>Veloran Business Card</title>
<link href="https://fonts.googleapis.com/css2?family=Questrial&family=Didact+Gothic&display=swap" rel="stylesheet">
<style>
  :root {
    --backdrop: #3a322d;
    --card: #1d1e20;
    --card-edge: #121314;
    --grey: #8a8b8d;
    --light: #e8e8e8;
    --orange: #f0941f;
    --divider: #5a5b5e;
  }
  * { margin: 0; padding: 0; box-sizing: border-box; }
  html, body { width: 1200px; height: 769px; overflow: hidden; }
  body {
    background: var(--backdrop);
    font-family: "Questrial", "Didact Gothic", sans-serif;
    position: relative;
  }
  .card {
    position: absolute;
    width: 540px;
    height: 310px;
    background: var(--card);
    border: 1px solid var(--card-edge);
    box-shadow: 0 14px 30px rgba(0,0,0,0.45);
  }
  .card-front { left: 40px; top: 230px; }
  .card-back { left: 620px; top: 230px; }

  /* front */
  .front-brand {
    position: absolute; left: 0; right: 0; top: 82px;
    display: flex; flex-direction: column; align-items: center;
  }
  .brand-dot {
    width: 74px; height: 74px; border-radius: 50%;
    background: var(--grey);
  }
  .front-name {
    margin-top: 14px;
    color: var(--grey);
    font-size: 30px; letter-spacing: 8px;
  }
  .front-web {
    margin-top: 16px;
    color: var(--light);
    font-size: 12px; letter-spacing: 5px;
  }

  /* back */
  .back-brand {
    position: absolute; left: 30px; width: 250px; top: 96px;
    display: flex; flex-direction: column; align-items: center;
  }
  .brand-dot-small {
    width: 52px; height: 52px; border-radius: 50%;
    background: var(--grey);
  }
  .back-name {
    margin-top: 8px;
    color: var(--grey);
    font-size: 38px; letter-spacing: 6px; line-height: 1;
  }
  .tagline {
    margin-top: 6px;
    color: var(--orange);
    font-size: 12.5px; letter-spacing: 0.3px;
  }
  .divider {
    position: absolute; left: 300px; top: 60px;
    width: 1px; height: 190px;
    background: linear-gradient(var(--card), var(--divider) 30%, var(--divider) 70%, var(--card));
  }
  .contact {
    position: absolute; left: 322px; top: 70px;
    color: var(--light);
  }
  .person-name {
    color: var(--orange);
    font-size: 20px; font-weight: 400; letter-spacing: 0.5px;
    font-family: "Didact Gothic", "Questrial", sans-serif;
  }
  .person-role { font-size: 13px; margin-top: 2px; }
  .address { font-size: 12.5px; line-height: 17px; margin-top: 6px; }
  .details { list-style: none; margin-top: 8px; }
  .details li {
    display: flex; align-items: center; gap: 8px;
    font-size: 12.5px; line-height: 18px;
  }
  .details svg { width: 11px; height: 11px; flex: none; fill: var(--orange); }
</style>
</head>
<body>
  <section class="card card-front">
    <div class="front-brand">
      <div class="brand-dot"></div>
      <div class="front-name">VELORAN</div>
      <div class="front-web">www.veloran.com</div>
    </div>
  </section>

  <section class="card card-back">
    <div class="back-brand">
      <div class="brand-dot-small"></div>
      <div class="back-name">VELORAN</div>
      <div class="tagline">Linking Partners - Shaping Insight</div>
    </div>
    <div class="divider"></div>
    <div class="contact">
      <div class="person-name">ERIK LINDQVIST</div>
      <div class="person-role">CEO/FOUNDER</div>
      <div class="address">2140 Harbor View Road<br>Juneau, Alaska 99801</div>
      <ul class="details">
        <li><svg viewBox="0 0 12 12" aria-hidden="true"><path d="M2.5 0.5l2 2.5-1.2 1.4c0.8 1.6 2 2.8 3.6 3.6L8.3 6.8l2.7 2-1 2.5C5 11 1 7 0.7 2z"/></svg>555 214 3069</li>
        <li><svg viewBox="0 0 12 12" aria-hidden="true"><path d="M3 0h6a1 1 0 0 1 1 1v10a1 1 0 0 1-1 1H3a1 1 0 0 1-1-1V1a1 1 0 0 1 1-1zm0.6 1.4v7.8h4.8V1.4z"/></svg>555 731 4820</li>
        <li><svg viewBox="0 0 12 12" aria-hidden="true"><path d="M3 0h5v3H3zM0 4h12v6H9v2H3v-2H0zm4 4v3h4V8z"/></svg>555 902 6157</li>
        <li><svg viewBox="0 0 12 12" aria-hidden="true"><path d="M0 2h12v1L6 7 0 3zm0 2.3l6 4 6-4V10H0z"/></svg>info@veloran.com</li>
        <li><svg viewBox="0 0 12 12" aria-hidden="true"><path d="M6 0a6 6 0 1 0 0 12A6 6 0 0 0 6 0zm0 1.3c0.8 0 1.6 1.9 1.7 4H4.3C4.4 3.2 5.2 1.3 6 1.3zM4.3 6.7h3.4C7.6 8.8 6.8 10.7 6 10.7S4.4 8.8 4.3 6.7z"/></svg>www.veloran.com</li>
      </ul>
    </div>
  </section>
</body>
</html>
```